Commercial janitorial cleaning

Janitorial cleaning particularly for commercial buildings. Website needs to specify free estimates. Location of service is Hudson, Valatie, East Greenbush, Troy, Albany ny area. Services page with Janitorial services- General Office Cleaning, Construction Cleaning, Carpet Extraction, Consultation/Business, Lighting Maintenance, Seasonal Deep Cleaning, Window cleaning, Event Cleaning, Floor and Carpet Cleaning, Floor Striping and Waxing. Contact us page with email phone number on page and a request page that emails me if they have any questions. About us page-the picture of my family on it with a section I can type a story myself.

Target Market(s)

Commercial businesses

Industry/Entity Type

Janitorial Service

Number of Pages Required

4 page

Font styles to use
Serif
Sans Serif
Script

Colors
ec1f27
1b1b1b
ffffff
9d9d9d

Requirements
Must have
• Phone number 555-314-2760. Must have free estimates on home page. Going for industrial / modern look to website
Nice to have
• Logo is a red and black building so if those colors could be coordinated to website that would be awesome.

```html
<!DOCTYPE html>
<html lang="en">
<head>
<meta charset="utf-8">
<title>Steadfast Cleaning Services – Commercial Janitorial Cleaning</title>
<link href="https://fonts.googleapis.com/css2?family=Dosis:wght@400;500;600;700&family=Open+Sans:ital,wght@0,400;0,600;0,700;1,400;1,700&display=swap" rel="stylesheet">
<style>
:root{
  --red:#ec1f27;
  --red-dark:#c9161d;
  --ink:#1b1b1b;
  --nav:#333333;
  --white:#ffffff;
  --grey:#9d9d9d;
  --text:#6b6b6b;
  --light:#f1f1f1;
  --line:#dcdcdc;
  --heading:'Dosis',sans-serif;
  --body:'Open Sans',sans-serif;
}
*{box-sizing:border-box;margin:0;padding:0}
html,body{width:1200px;height:2880px;overflow:hidden}
body{background:var(--white);font-family:var(--body);color:var(--text);position:relative}
.abs{position:absolute}

/* header */
.site-header{position:absolute;top:0;left:0;width:1200px;height:144px;background:var(--white)}
.brand{position:absolute;left:100px;top:36px;display:flex;align-items:center;gap:14px}
.brand-mark{width:40px;height:70px;background:var(--red)}
.brand-name{font-family:var(--heading);font-weight:600;color:var(--red);line-height:1.05}
.brand-name .top{font-size:32px;letter-spacing:.5px;text-transform:uppercase;display:block}
.brand-name .sub{font-size:25px;display:block}
.header-phone{position:absolute;left:695px;top:44px;display:flex;align-items:center;gap:14px}
.header-phone .label{font-family:var(--body);font-size:16px;color:var(--red);display:block;line-height:1}
.header-phone .num{font-family:var(--heading);font-size:27px;font-weight:500;color:var(--ink);display:block;line-height:1.2}
.btn-estimate{position:absolute;left:954px;top:52px;width:146px;height:36px;background:var(--red);color:var(--white);font-family:var(--heading);font-weight:700;font-size:17px;display:flex;align-items:center;justify-content:center;border-radius:2px}

/* nav */
.main-nav{position:absolute;top:144px;left:0;width:1200px;height:56px;background:var(--nav)}
.main-nav .home-tab{position:absolute;left:0;top:0;height:56px;width:200px;background:var(--red);clip-path:polygon(0 0,176px 0,200px 28px,176px 56px,0 56px)}
.main-nav ul{list-style:none;position:absolute;left:98px;top:0;height:56px;display:flex;align-items:center;gap:0}
.main-nav li{font-family:var(--heading);font-weight:600;font-size:15px;color:var(--white);text-transform:uppercase;letter-spacing:.3px}
.main-nav li:nth-child(1){width:104px}
.main-nav li:nth-child(2){width:120px}
.main-nav li:nth-child(3){width:148px}
.main-nav li:nth-child(4){width:156px}
.main-nav li:nth-child(5){width:118px}
.main-nav li:nth-child(6){width:86px}

/* hero */
.hero{position:absolute;top:200px;left:0;width:1200px;height:495px;overflow:hidden}
.hero-photo{position:absolute;inset:0;background:
  radial-gradient(ellipse 260px 200px at 640px 260px,rgba(240,200,20,.85),rgba(240,200,20,0) 70%),
  radial-gradient(ellipse 140px 200px at 1000px 250px,rgba(245,210,30,.9),rgba(245,210,30,0) 75%),
  linear-gradient(180deg,#6d7378 0%,#9aa0a4 45%,#4c4f52 100%)}
.hero-shade{position:absolute;inset:0;background:linear-gradient(90deg,rgba(20,20,20,.55) 0%,rgba(20,20,20,0) 55%)}
.hero h1{position:absolute;left:98px;top:158px;font-family:var(--heading);color:var(--white);font-weight:700;line-height:1}
.hero h1 .l1{display:block;font-size:52px;letter-spacing:1px}
.hero h1 .l2{display:block;font-size:34px;font-weight:600;margin-top:12px;letter-spacing:.5px}
.btn-red{position:absolute;left:98px;top:270px;width:108px;height:32px;background:var(--red);color:var(--white);font-family:var(--heading);font-weight:700;font-size:14px;display:flex;align-items:center;justify-content:center;border-radius:3px}
.hero-dots{position:absolute;left:100px;top:329px;display:flex;gap:8px;align-items:center}
.hero-dots span{width:10px;height:10px;border-radius:50%;background:var(--white)}
.hero-dots span.on{width:16px;height:16px;border:3px solid var(--white);background:transparent}

/* welcome */
.welcome{position:absolute;top:695px;left:0;width:1200px;height:453px}
.mascot{position:absolute;left:119px;top:73px;width:284px;height:298px;background:radial-gradient(circle at 45% 40%,#2f4c8c 0%,#28407a 40%,#e7ecf3 72%,#ffffff 100%);border-radius:50%}
.welcome-text{position:absolute;left:461px;top:108px;width:640px}
.welcome-text h2{font-family:var(--heading);font-weight:400;font-size:31px;line-height:1.2;color:var(--ink)}
.welcome-text h2 span{display:block;color:var(--red);text-transform:uppercase}
.welcome-text p{font-size:11.5px;line-height:19px;margin-top:12px}
.welcome-text p:first-of-type{margin-top:14px}
.btn-outline{display:inline-flex;align-items:center;gap:5px;height:26px;padding:0 8px;border:1px solid #bcbcbc;font-family:var(--body);font-size:10.5px;color:#444;text-transform:uppercase;margin-top:20px;border-radius:2px}
.btn-outline i{width:10px;height:10px;border-radius:50%;background:#444;display:inline-block;position:relative}
.btn-outline i::after{content:"";position:absolute;left:3px;top:3px;border-left:4px solid #fff;border-top:2px solid transparent;border-bottom:2px solid transparent}

/* wave edges */
.wave{position:absolute;left:0;width:1200px;height:22px}

/* services */
.services{position:absolute;top:1148px;left:0;width:1200px;height:528px;background:var(--light)}
.section-title{position:absolute;left:0;width:1200px;text-align:center;font-family:var(--heading);font-weight:500;font-size:33px;color:var(--ink);text-transform:uppercase;letter-spacing:.5px}
.services .section-title{top:64px}
.service-card{position:absolute;top:183px;width:238px;height:261px;background:var(--white);border:1px solid #e4e4e4}
.service-card .icon{position:absolute;left:71px;top:-30px;width:96px;height:96px;border-radius:50%;display:flex;align-items:center;justify-content:center}
.icon.red{background:var(--red)}
.icon.dark{background:#333}
.service-card h3{position:absolute;top:80px;width:100%;text-align:center;font-family:var(--heading);font-weight:500;font-size:20px;color:var(--ink)}
.service-card p{position:absolute;top:114px;left:20px;right:20px;text-align:center;font-size:10.5px;line-height:17px}
.service-card .more{position:absolute;left:0;bottom:0;width:100%;height:40px;border-top:1px solid #e4e4e4;display:flex;align-items:center;justify-content:center;gap:14px;font-family:var(--body);font-size:10.5px;color:#555;text-transform:uppercase}
.slider-arrow{position:absolute;top:280px}

/* commercial */
.commercial{position:absolute;top:1676px;left:0;width:1200px;height:542px}
.commercial .section-title{top:58px;font-size:31px}
.work{position:absolute;top:144px;width:313px}
.work .photo{width:309px;height:183px;border:3px solid #eee}
.work h3{font-family:var(--heading);font-weight:500;font-size:20px;color:var(--ink);margin-top:22px}
.work p{font-size:10.5px;line-height:17px;margin-top:6px;width:300px}
.work .btn-outline{margin-top:10px;text-transform:none;font-size:11.5px;height:28px}

/* testimonial */
.testimonial{position:absolute;top:2218px;left:0;width:1200px;height:322px;background:
  linear-gradient(135deg,rgba(255,255,255,.05) 0%,rgba(255,255,255,0) 40%),var(--red)}
.testimonial blockquote{position:absolute;left:130px;top:88px;width:940px;text-align:center;color:var(--white);font-style:italic;font-size:13.5px;line-height:24px}
.testimonial cite{position:absolute;left:0;top:180px;width:1200px;text-align:center;color:var(--white);font-style:italic;font-size:13.5px}
.testimonial cite b{font-weight:700}
.t-dots{position:absolute;left:546px;top:224px;display:flex;gap:6px}
.t-dots span{width:44px;height:4px;background:rgba(255,255,255,.35)}
.t-dots span.on{background:var(--white)}

/* footer */
.site-footer{position:absolute;top:2540px;left:0;width:1200px;height:278px;background:#f4f4f4}
.footer-brand{position:absolute;left:100px;top:36px;display:flex;align-items:center;gap:12px}
.footer-brand .brand-mark{width:30px;height:54px}
.footer-brand .brand-name .top{font-size:24px}
.footer-brand .brand-name .sub{font-size:19px}
.footer-about{position:absolute;left:100px;top:112px;width:240px;font-size:10.5px;line-height:17px;color:#555}
.social{position:absolute;left:100px;top:192px;display:flex;gap:6px}
.social span{width:24px;height:24px;border:1px solid #777;border-radius:50%}
.footer-col h4{font-family:var(--heading);font-weight:500;font-size:18px;color:var(--ink);text-transform:uppercase;letter-spacing:.3px}
.footer-col{position:absolute;top:46px}
.newsletter{left:401px;width:260px}
.newsletter p{font-size:10.5px;line-height:17px;margin-top:14px;color:#555}
.newsletter .field{margin-top:12px;width:245px;height:40px;border:1px solid #ddd;background:var(--white);font-size:10.5px;color:#555;padding:0 12px;display:flex;align-items:center}
.newsletter .submit{margin-top:10px;width:120px;height:34px;background:var(--red);color:var(--white);font-family:var(--body);font-size:11.5px;font-weight:600;display:flex;align-items:center;justify-content:center;text-transform:uppercase}
.contact{left:708px;width:270px}
.contact ul{list-style:none;margin-top:20px}
.contact li{display:flex;gap:12px;font-size:11.5px;line-height:19px;color:#555;margin-bottom:10px}
.contact li svg{flex:none;margin-top:3px}
.links{left:1000px}
.links ul{list-style:none;margin-top:14px}
.links li{font-size:10.5px;line-height:26px;color:#555}
.bottom-bar{position:absolute;top:2818px;left:0;width:1200px;height:62px;background:var(--white);border-top:1px solid #e3e3e3;text-align:center;font-size:10.5px;color:#555;line-height:34px}
</style>
</head>
<body>

<header class="site-header">
  <div class="brand">
    <span class="brand-mark"></span>
    <div class="brand-name"><span class="top">Steadfast</span><span class="sub">Cleaning Services</span></div>
  </div>
  <div class="header-phone">
    <svg width="30" height="30" viewBox="0 0 24 24"><path fill="#1b1b1b" d="M6.6 10.8a15.1 15.1 0 0 0 6.6 6.6l2.2-2.2c.3-.3.7-.4 1-.2 1.1.4 2.3.6 3.6.6.6 0 1 .4 1 1V20c0 .6-.4 1-1 1A17 17 0 0 1 3 4c0-.6.4-1 1-1h3.5c.6 0 1 .4 1 1 0 1.3.2 2.5.6 3.6.1.3 0 .7-.2 1z"/></svg>
    <div><span class="label">Request Appointment</span><span class="num">555-314-2760</span></div>
  </div>
  <div class="btn-estimate">FREE ESTIMATE</div>
</header>

<nav class="main-nav">
  <div class="home-tab"></div>
  <ul>
    <li>Home</li><li>About Us</li><li>Our Services</li><li>Free Estimate</li><li>Projects</li><li>Blog</li><li>Contact Us</li>
  </ul>
</nav>

<section class="hero">
  <div class="hero-photo" role="img" aria-label="Yellow mop bucket and wet floor caution sign on a polished commercial floor"></div>
  <div class="hero-shade"></div>
  <h1><span class="l1">COMMERCIAL</span><span class="l2">JANITORIAL CLEANING</span></h1>
  <div class="btn-red">READ MORE</div>
  <div class="hero-dots"><span class="on"></span><span></span><span></span><span></span></div>
</section>

<section class="welcome">
  <div class="mascot" role="img" aria-label="Cartoon cleaner in blue uniform holding a vacuum hose"></div>
  <div class="welcome-text">
    <h2>WELCOME TO<span>Steadfast Cleaning Services</span></h2>
    <p>Sed ut perspiciatis unde omnis iste natus error sit voluptatem accusantium doloremque laudantium, totam rem aperiam, eaque ipsa quae ab illo inventore veritatis et quasi architecto beatae vitae dicta sunt explicabo. Nemo enim ipsam voluptatem quia voluptas sit aspernatur aut odit aut fugit, sed quia consequuntur magni dolores</p>
    <p>Sed ut perspiciatis unde omnis iste natus error sit voluptatem accusantium doloremque laudantium, totam rem aperiam, eaque ipsa quae ab illo inventore veritatis et quasi architecto beatae vitae dicta sunt explicabo. Nemo enim ipsam voluptatem quia voluptas sit aspernatur aut odit aut fugit, sed quia consequuntur magni dolores</p>
    <span class="btn-outline">Read more <i></i></span>
  </div>
</section>

<section class="services">
  <svg class="wave" style="top:-10px" viewBox="0 0 1200 22" preserveAspectRatio="none">
    <defs><pattern id="scallop" width="40" height="22" patternUnits="userSpaceOnUse"><path d="M0 10 Q10 0 20 10 T40 10 V22 H0 Z" fill="#f1f1f1"/></pattern></defs>
    <rect width="1200" height="22" fill="url(#scallop)"/>
  </svg>
  <h2 class="section-title">Our Services</h2>

  <svg class="slider-arrow" style="left:38px" width="30" height="60" viewBox="0 0 30 60"><path d="M26 2 L4 30 L26 58" fill="none" stroke="#c8c8c8" stroke-width="2"/></svg>
  <svg class="slider-arrow" style="left:1134px" width="30" height="60" viewBox="0 0 30 60"><path d="M4 2 L26 30 L4 58" fill="none" stroke="#c8c8c8" stroke-width="2"/></svg>

  <article class="service-card" style="left:98px">
    <div class="icon red"><svg width="40" height="40" viewBox="0 0 40 40" fill="none" stroke="#fff" stroke-width="2.5"><circle cx="16" cy="9" r="4"/><path d="M16 14v12M10 36l6-10 6 10M30 4v26M26 36h8l-4-6z"/></svg></div>
    <h3>Office Cleaning</h3>
    <p>Sed ut perspiciatis unde omnis iste natus error sit voluptatem accusantium doloremque laudantium, totam rem aperiam, eaque ipsa quae</p>
    <div class="more">Read more <span>&#8600;</span></div>
  </article>
  <article class="service-card" style="left:351px">
    <div class="icon dark"><svg width="40" height="40" viewBox="0 0 40 40" fill="none" stroke="#fff" stroke-width="2.5"><path d="M30 4 Q8 6 14 26"/><circle cx="20" cy="30" r="7"/><path d="M8 36h24"/></svg></div>
    <h3>Construction Cleaning</h3>
    <p>Sed ut perspiciatis unde omnis iste natus error sit voluptatem accusantium doloremque laudantium, totam rem aperiam, eaque ipsa quae</p>
    <div class="more">Read more <span>&#8600;</span></div>
  </article>
  <article class="service-card" style="left:604px">
    <div class="icon red"><svg width="40" height="40" viewBox="0 0 40 40" fill="none" stroke="#fff" stroke-width="2.5"><rect x="8" y="8" width="24" height="24"/><path d="M12 14h16M12 20h16M12 26h16M4 12v16M36 12v16"/></svg></div>
    <h3>Carpet Extraction</h3>
    <p>Sed ut perspiciatis unde omnis iste natus error sit voluptatem accusantium doloremque laudantium, totam rem aperiam, eaque ipsa quae</p>
    <div class="more">Read more <span>&#8600;</span></div>
  </article>
  <article class="service-card" style="left:857px">
    <div class="icon dark"><svg width="40" height="40" viewBox="0 0 40 40" fill="none" stroke="#fff" stroke-width="2.5"><rect x="14" y="4" width="22" height="22"/><path d="M25 4v22M14 15h22"/><circle cx="8" cy="14" r="3"/><path d="M8 18v12M4 36l4-6 4 6"/></svg></div>
    <h3>Window Cleaning</h3>
    <p>Sed ut perspiciatis unde omnis iste natus error sit voluptatem accusantium doloremque laudantium, totam rem aperiam, eaque ipsa quae</p>
    <div class="more">Read more <span>&#8600;</span></div>
  </article>
</section>

<section class="commercial">
  <h2 class="section-title">Commercial Janitorial Cleaning</h2>
  <article class="work" style="left:98px">
    <div class="photo" role="img" aria-label="Worker servicing ceiling lights in an office hallway" style="background:linear-gradient(160deg,#9aa9c4 0%,#5a6a8a 50%,#2e3648 100%)"></div>
    <h3>Lighting Maintenance</h3>
    <p>Sed ut perspiciatis unde omnis iste natus error sit voluptatem accusantium doloremque laudantium, totam rem aperiam, eaque ipsa quae ab illo</p>
    <span class="btn-outline">Learn More <i></i></span>
  </article>
  <article class="work" style="left:443px">
    <div class="photo" role="img" aria-label="Crew cleaning an event venue under pink stage lights" style="background:radial-gradient(circle at 40% 30%,#f26aa0 0%,#b0246a 40%,#3a0f2a 100%)"></div>
    <h3>Event Cleaning</h3>
    <p>Sed ut perspiciatis unde omnis iste natus error sit voluptatem accusantium doloremque laudantium, totam rem aperiam, eaque ipsa quae ab illo</p>
    <span class="btn-outline">Learn More <i></i></span>
  </article>
  <article class="work" style="left:789px">
    <div class="photo" role="img" aria-label="Two team members on a ladder in front of garden greenery" style="background:linear-gradient(135deg,#3d5a2a 0%,#7a8a4a 45%,#b58a6a 70%,#4a3a2a 100%)"></div>
    <h3>Seasonal Deep Cleaning</h3>
    <p>Sed ut perspiciatis unde omnis iste natus error sit voluptatem accusantium doloremque laudantium, totam rem aperiam, eaque ipsa quae ab illo</p>
    <span class="btn-outline">Learn More <i></i></span>
  </article>
</section>

<section class="testimonial">
  <svg class="wave" style="top:-10px" viewBox="0 0 1200 22" preserveAspectRatio="none">
    <defs><pattern id="scallopRed" width="40" height="22" patternUnits="userSpaceOnUse"><path d="M0 10 Q10 0 20 10 T40 10 V22 H0 Z" fill="#ec1f27"/></pattern></defs>
    <rect width="1200" height="22" fill="url(#scallopRed)"/>
  </svg>
  <blockquote>&ldquo; Lorem ipsum dolor sit amet, consectetur adipiscing elit, sed do eiusmod tempor incididunt ut labore et dolore magna aliqua. Ut enim ad minim veniam, quis nostrud exercitation ullamco laboris nisi ut aliquip ex ea commodo consequat. Duis aute irure dolor in reprehenderit in voluptate velit esse cillum dolore eu fugiat nulla pariatur. Excepteur sint occaecat &rdquo;</blockquote>
  <cite><b>Jane Rowe</b> - Steadfast Cleaning Services</cite>
  <div class="t-dots"><span class="on"></span><span></span><span></span></div>
</section>

<footer class="site-footer">
  <div class="footer-brand">
    <span class="brand-mark"></span>
    <div class="brand-name"><span class="top">Steadfast</span><span class="sub">Cleaning Services</span></div>
  </div>
  <p class="footer-about">Sed ut perspiciatis unde omnis iste natus error sit voluptatem accusantium doloremque laudantium, totam rem aperiam, eaque ipsa quae ab illo inventore</p>
  <div class="social"><span></span><span></span><span></span><span></span></div>

  <div class="footer-col newsletter">
    <h4>Sign up for newsletter</h4>
    <p>Excepteur sint occaecat cupidatat non proident, sunt in culpa qui officia deserunt</p>
    <div class="field">Enter email</div>
    <div class="submit">Subscription</div>
  </div>

  <div class="footer-col contact">
    <h4>Contact Us</h4>
    <ul>
      <li><svg width="12" height="14" viewBox="0 0 12 16"><path fill="#555" d="M6 0a6 6 0 0 0-6 6c0 4.5 6 10 6 10s6-5.5 6-10a6 6 0 0 0-6-6zm0 8.5A2.5 2.5 0 1 1 6 3.5a2.5 2.5 0 0 1 0 5z"/></svg><span>Steadfast Cleaning Services<br>4820 Harbor Ln, Suite 210,<br>Hudson, NY 12534</span></li>
      <li><svg width="13" height="13" viewBox="0 0 24 24"><path fill="#555" d="M6.6 10.8a15.1 15.1 0 0 0 6.6 6.6l2.2-2.2c.3-.3.7-.4 1-.2 1.1.4 2.3.6 3.6.6.6 0 1 .4 1 1V20c0 .6-.4 1-1 1A17 17 0 0 1 3 4c0-.6.4-1 1-1h3.5c.6 0 1 .4 1 1 0 1.3.2 2.5.6 3.6.1.3 0 .7-.2 1z"/></svg><span>Phone: 555-314-2760</span></li>
      <li><svg width="13" height="11" viewBox="0 0 16 12"><path fill="#555" d="M0 0h16v12H0z"/><path d="M0 0l8 6 8-6" fill="none" stroke="#f4f4f4" stroke-width="1.5"/></svg><span>info@steadfastcleaning.com</span></li>
    </ul>
  </div>

  <div class="footer-col links">
    <h4>Quick Links</h4>
    <ul><li>Home</li><li>About Us</li><li>Services</li><li>Get A Quote</li><li>Blog</li><li>Contact Us</li></ul>
  </div>
</footer>

<div class="bottom-bar">&copy;2017 Steadfast Cleaning Services . All Rights Reserved.</div>

</body>
</html>
```